PWR Business Card

Looking for a business card for my restaurant group I own. Four different concepts:

Copperleaf Alehouse
Bramble Alehouse
Hollister's Wood Fired Grill
Fenwick Patty Company

Card doesn't need to include all the logos.

```html
<!DOCTYPE html>
<html lang="en">
<head>
<meta charset="utf-8">
<title>PWR Business Card</title>
<link href="https://fonts.googleapis.com/css2?family=Lato:wght@400;700;900&display=swap" rel="stylesheet">
<style>
  :root {
    --stage: #2e2e2e;
    --gold: #cfae6e;
    --gold-light: #dcc08a;
    --ink: #111111;
    --grey: #6f6f6f;
    --faint: #efefef;
    --paper: #ffffff;
  }
  * { box-sizing: border-box; margin: 0; padding: 0; }
  html, body { width: 1200px; height: 866px; overflow: hidden; }
  body {
    background: var(--stage);
    font-family: "Lato", sans-serif;
    position: relative;
  }
  .card {
    position: absolute;
    top: 278px;
    width: 540px;
    height: 310px;
    overflow: hidden;
    box-shadow: 0 8px 24px rgba(0,0,0,.45);
  }
  .card--front { left: 40px; background: var(--paper); border-bottom: 8px solid var(--gold); }
  .card--back { left: 620px; background: var(--gold); }

  .watermark {
    position: absolute;
    font-weight: 900;
    letter-spacing: 6px;
    line-height: 1;
    pointer-events: none;
  }
  .card--front .watermark { top: -20px; left: 70px; font-size: 200px; color: var(--faint); }
  .card--back .watermark { top: -30px; left: 90px; font-size: 210px; color: var(--gold-light); }

  .holder { position: absolute; left: 34px; top: 40px; }
  .holder__name { color: var(--gold); font-weight: 900; font-size: 20px; letter-spacing: 1.5px; text-transform: uppercase; }
  .holder__title { color: var(--ink); font-size: 14px; margin-top: 2px; }
  .contact { list-style: none; margin-top: 10px; }
  .contact li { display: flex; align-items: center; gap: 7px; font-size: 14px; color: var(--ink); line-height: 1.45; }
  .contact svg { width: 11px; height: 11px; fill: var(--gold); flex: none; }

  .brand { position: absolute; right: 36px; top: 78px; text-align: right; color: var(--gold); font-weight: 700; }
  .brand__mark { font-size: 38px; letter-spacing: 4px; line-height: 1; }
  .brand__name { font-size: 34px; letter-spacing: 5px; line-height: 1.05; margin-top: 4px; }
  .brand__tag { font-size: 15px; letter-spacing: 5px; line-height: 1.3; margin-top: 2px; }

  .rule { position: absolute; left: 34px; right: 34px; top: 204px; height: 1px; background: var(--grey); }

  .address { position: absolute; right: 36px; bottom: 24px; text-align: right; font-size: 15px; font-style: normal; color: var(--ink); line-height: 1.4; }

  .back-mark {
    position: absolute; left: 0; right: 0; top: 110px; text-align: center;
    font-weight: 900; font-size: 64px; letter-spacing: 6px; color: var(--ink); line-height: 1;
  }
  .venues {
    position: absolute; left: 0; right: 0; bottom: 54px; text-align: center;
    font-weight: 900; font-size: 12.5px; letter-spacing: .5px; color: var(--ink); text-transform: uppercase; line-height: 1.6;
  }
</style>
</head>
<body>
  <section class="card card--front">
    <div class="watermark" aria-hidden="true">PWR</div>
    <div class="holder">
      <p class="holder__name">Daniel Rowe</p>
      <p class="holder__title">Managing Director</p>
      <ul class="contact">
        <li><svg viewBox="0 0 12 12"><path d="M2 1h2.5l1 3-1.5 1a6 6 0 0 0 3 3l1-1.5 3 1V10a1 1 0 0 1-1 1A9 9 0 0 1 1 2a1 1 0 0 1 1-1z"/></svg>044-555 210 347</li>
        <li><svg viewBox="0 0 12 12"><path d="M0 2h12v8H0zM1 3l5 4 5-4v-.2H1z" fill-rule="evenodd"/></svg>hello@prescottgroup.com</li>
        <li><svg viewBox="0 0 12 12"><circle cx="6" cy="6" r="6"/></svg>www.prescottgroup.com</li>
      </ul>
    </div>
    <div class="brand">
      <p class="brand__mark">PWR</p>
      <p class="brand__name">PRESCOTT</p>
      <p class="brand__tag">HOSPITALITY GROUP</p>
    </div>
    <div class="rule"></div>
    <address class="address">88 Harbor Lane,<br>Springvale, 40318</address>
  </section>

  <section class="card card--back">
    <div class="watermark" aria-hidden="true">PWR</div>
    <p class="back-mark">PWR</p>
    <p class="venues">Copperleaf Alehouse | Bramble Alehouse<br>Hollister's Wood Fired Grill | Fenwick Patty Company</p>
  </section>
</body>
</html>
```